The Birchwater Evenings - Concert Series Website Design

I've recently decided to launch a concert series in my living room and would love a website to use to promote the series. I'm looking for a simple Wix design that I could take over once it's complete. I'll provide the logo for which I'd like the website to utilize the color scheme.

Target Market(s)

Music lovers in Denver

Industry/Entity Type

Music

Coding

Coded - Design and coding required

Number of Pages Required

2 page

Font styles to use
Script

Requirements
Must have
• 2 pages - one for concert goers to see the schedule and rsvp, and one for artists about the booking process

```html
<!DOCTYPE html>
<html lang="en">
<head>
<meta charset="utf-8">
<title>The Birchwater Evenings</title>
<link href="https://fonts.googleapis.com/css2?family=Forum&family=Montserrat:wght@400;500;600;700&family=Raleway:wght@400;500;600&display=swap" rel="stylesheet">
<style>
:root{
  --cream:#fff7ec;
  --maroon:#6e1a26;
  --maroon-text:#7a1f2e;
  --red:#c8343e;
  --orange:#fdb95a;
  --ink:#2a2a2a;
  --white:#ffffff;
  --dark-top:#1e0a0d;
  --purple:#2d0a45;
  --mauve:#9a4a72;
  --black:#000000;
  --gold:#f5b400;
}
*{margin:0;padding:0;box-sizing:border-box}
html,body{width:1200px;height:4324px;overflow:hidden}
body{position:relative;background:var(--cream);font-family:"Montserrat",sans-serif;color:var(--ink)}
.abs{position:absolute}
.display{font-family:"Forum",serif;font-weight:400}
.topline{left:0;top:0;width:1200px;height:3px;background:linear-gradient(90deg,var(--orange),var(--red),var(--purple))}
.brand{font-family:"Forum",serif;color:var(--maroon);line-height:.9;display:flex;align-items:center;gap:10px}
.brand .dot{width:14px;height:14px;border-radius:50%;background:var(--maroon)}
.nav a{position:absolute;top:40px;font-family:"Forum",serif;font-size:16px;color:var(--maroon);text-decoration:none;letter-spacing:.5px}
.btn{display:flex;align-items:center;justify-content:center;border-radius:40px;font-family:"Forum",serif;text-decoration:none;letter-spacing:.5px}
.btn-maroon{background:var(--maroon);color:var(--orange)}
.btn-white{background:var(--white);color:var(--maroon)}
.hero{left:0;top:97px;width:1200px;height:678px;background:linear-gradient(120deg,#2a0f22 0%,#5a2238 35%,#a54a4a 60%,#3a1a2e 100%)}
.hero-shade{left:0;top:97px;width:660px;height:678px;background:linear-gradient(90deg,rgba(20,5,15,.7),rgba(20,5,15,0))}
.hero-kicker{left:109px;top:234px;font-size:29px;color:var(--white);letter-spacing:2px}
.hero-title{left:107px;top:262px;font-size:86px;line-height:.88;color:var(--white);letter-spacing:1px}
.hero-sub{left:110px;top:416px;font-size:15px;line-height:25px;color:var(--white);font-weight:500;width:380px}
.hero-btn{left:109px;top:485px;width:252px;height:55px;border:3px solid var(--white);background:var(--maroon);color:var(--orange);font-size:18px}
.rsvp{left:153px;top:646px;width:894px;height:297px;background:var(--orange);border-radius:34px;text-align:center}
.rsvp h2{margin-top:36px;font-size:31px;line-height:40px;color:var(--ink)}
.rsvp p{margin-top:16px;font-size:14px;line-height:25px;font-weight:500;color:var(--ink)}
.field{top:203px;width:196px;height:50px;background:var(--white);border-radius:25px;display:flex;align-items:center;justify-content:space-between;padding:0 20px;font-size:12px;font-weight:500;color:var(--ink)}
.submit{left:661px;top:203px;width:196px;height:50px;font-size:16px}
.badge{left:111px;top:1057px;width:419px;height:487px;display:flex;flex-direction:column;align-items:center;justify-content:center;text-align:center}
.badge .name{font-family:"Forum",serif;color:var(--maroon);font-size:54px;line-height:1}
.about{left:597px;top:1040px;width:490px}
.about h2{font-size:44px;color:var(--maroon-text)}
.about .lead{margin-top:12px;color:var(--red);font-size:17px;line-height:29px;font-weight:500}
.about p.body{margin-top:18px;font-family:"Raleway",sans-serif;font-size:13.5px;line-height:25.7px;text-align:justify;color:#333}
.about p.body+p.body{margin-top:26px}
.readmore{left:599px;top:1505px;width:148px;height:54px;font-size:16px}
.peaks{left:0;top:1586px;width:1200px;height:430px;background:linear-gradient(180deg,var(--cream) 0%,#8b8a8e 30%,#4a3a3a 55%,#d9782a 72%,#3a1e14 100%)}
.shows{left:0;top:1963px;width:1200px;height:1171px;border-radius:70px 70px 0 0;background:linear-gradient(180deg,var(--dark-top) 0%,var(--purple) 45%,var(--mauve) 100%)}
.shows h2{position:absolute;left:0;width:1200px;top:72px;text-align:center;font-size:52px;color:var(--white);letter-spacing:1px}
.shows .intro{position:absolute;left:0;width:1200px;top:154px;text-align:center;font-size:16px;font-weight:600;color:var(--white);letter-spacing:1px}
.show{left:111px;width:978px;height:236px;border:1.5px solid rgba(255,255,255,.45);border-radius:20px;background:rgba(255,255,255,.06)}
.show .photo{position:absolute;left:11px;top:12px;width:298px;height:210px;border-radius:14px 40px 14px 40px}
.show .info{position:absolute;left:347px;top:44px;color:var(--white)}
.show h3{font-size:26px;font-weight:500;letter-spacing:.5px}
.show .role{margin-top:14px;font-size:14px;font-weight:600;letter-spacing:1px}
.show .desc{margin-top:18px;font-size:14px}
.show .link{display:inline-block;margin-top:16px;font-size:18px;font-weight:600;color:var(--white);text-decoration:underline;text-underline-offset:4px}
.all-shows{left:500px;top:3002px;width:200px;height:55px;font-size:16px}
.reviews-title{left:0;width:1200px;top:3210px;text-align:center;font-size:50px;color:var(--maroon-text);letter-spacing:1px}
.review{top:3309px;width:444px;height:277px;background:var(--white);border-radius:28px;padding:28px 32px}
.review .stars{display:flex;gap:3px}
.review .quote{position:absolute;right:26px;top:4px;font-family:"Forum",serif;font-size:96px;color:var(--maroon-text);line-height:1}
.review h4{margin-top:20px;font-family:"Raleway",sans-serif;font-size:15px;font-weight:600;color:var(--ink)}
.review p{margin-top:12px;font-family:"Raleway",sans-serif;font-size:13px;line-height:25.5px;color:#555}
.review .sign{position:absolute;left:32px;bottom:30px;font-family:"Raleway",sans-serif;font-size:16px;font-weight:600;color:var(--ink)}
.dots{left:540px;top:3642px;display:flex;gap:8px;align-items:center}
.dots span{width:6px;height:6px;border-radius:50%;background:#999}
.dots .on{width:16px;height:16px;border:2px solid var(--maroon);background:radial-gradient(var(--maroon) 35%,transparent 40%)}
.footer{left:0;top:3932px;width:1200px;height:392px;background:var(--black)}
.cta{left:111px;top:3765px;width:976px;height:334px;border-radius:167px;background:linear-gradient(180deg,#2a0840 0%,#7a2a5a 100%);text-align:center;color:var(--white)}
.cta h2{margin-top:52px;font-size:48px;line-height:57px;letter-spacing:1px}
.cta p{margin-top:24px;font-size:15px;font-weight:600;letter-spacing:.6px}
.cta-btn{left:482px;top:3994px;width:235px;height:54px;font-size:17px}
.foot-brand{left:201px;top:4190px;color:var(--white);font-size:30px}
.foot-brand .dot{background:var(--white)}
.foot-links a{position:absolute;top:4188px;font-family:"Forum",serif;font-size:19px;color:var(--white);text-decoration:none}
.copy{left:596px;top:4232px;font-family:"Forum",serif;font-size:18px;color:var(--white)}
</style>
</head>
<body>
<svg width="0" height="0" style="position:absolute">
  <defs><path id="star" d="M6.5 0l1.9 4.2 4.6.4-3.5 3 1 4.4-4-2.4-4 2.4 1-4.4-3.5-3 4.6-.4z"/></defs>
</svg>
<div class="abs topline"></div>

<header>
  <div class="abs brand" style="left:109px;top:24px;font-size:27px">
    <span class="dot"></span><span>The Birchwater<br>Evenings</span>
  </div>
  <nav class="nav">
    <a href="#" style="left:672px">HOME</a>
    <a href="#" style="left:775px">ABOUT THE SERIES</a>
  </nav>
  <a href="#" class="abs btn btn-maroon" style="left:960px;top:29px;width:127px;height:42px;font-size:15px">CONTACT US</a>
</header>

<section>
  <div class="abs hero" role="img" aria-label="Photo of musicians with a double bass performing to a small crowd in a warmly lit living room"></div>
  <div class="abs hero-shade"></div>
  <div class="abs display hero-kicker">WELCOME TO THE</div>
  <h1 class="abs display hero-title">BIRCHWATER<br>EVENINGS</h1>
  <p class="abs hero-sub">An intimate living-room concert series in the heart of Denver.</p>
  <a href="#" class="abs btn hero-btn">VIEW UPCOMING SHOWS</a>

  <form class="abs rsvp">
    <h2 class="display">JOIN US FOR AN<br>EVENING OF MUSIC AND BIRCHWATER</h2>
    <p>Please complete the form below to reserve your spot. Exact address and<br>event details will be emailed after your RSVP.</p>
    <div class="abs field" style="left:35px"><span>Name</span>
      <svg width="14" height="14" viewBox="0 0 14 14"><circle cx="7" cy="4" r="3" fill="#bbb"/><path d="M1 14c0-4 3-6 6-6s6 2 6 6z" fill="#bbb"/></svg></div>
    <div class="abs field" style="left:245px"><span>Email</span>
      <svg width="15" height="11" viewBox="0 0 15 11"><rect width="15" height="11" rx="1" fill="#bbb"/><path d="M1 1l6.5 5L14 1" stroke="#fff" fill="none"/></svg></div>
    <div class="abs field" style="left:453px"><span>No. of Guests</span>
      <svg width="18" height="13" viewBox="0 0 18 13"><circle cx="5" cy="4" r="2.5" fill="#bbb"/><circle cx="13" cy="4" r="2.5" fill="#bbb"/><circle cx="9" cy="5" r="3" fill="#999"/><path d="M2 13c0-3 3-5 7-5s7 2 7 5z" fill="#999"/></svg></div>
    <a href="#" class="abs btn btn-maroon submit">SUBMIT</a>
  </form>
</section>

<section>
  <div class="abs badge"><span class="name">The Birchwater<br>Evenings</span></div>
  <div class="abs about">
    <h2 class="display">ABOUT US</h2>
    <p class="lead">I'm delighted to announce the launch of The Birchwater Evenings: Intimate concerts in Denver's North End</p>
    <p class="body">Inspired by the quiet radiance that settles over the mountains at dusk, The Birchwater Evenings is a new living room concert series devoted to attentive listening, artistic depth, and shared musical experience. Hosted in my home in Denver's North End of Central Park, these gatherings will bring folks together for evenings of warmth, nuance, and connection.</p>
    <p class="body">With an audience of just 25–40 guests, each concert is designed to foster closeness between performer and listener. Expect thoughtful, engaging performances — music that glows in the quiet. This series is built on a simple conviction: extraordinary music does not require a grand hall. It requires space, intention, &amp; a community willing to listen.</p>
  </div>
  <a href="#" class="abs btn btn-maroon readmore">READ MORE</a>
</section>

<div class="abs peaks" role="img" aria-label="Snowy mountain range with the sun setting behind the peaks"></div>

<section class="abs shows">
  <h2 class="display">UPCOMING SHOWS</h2>
  <p class="intro">Discover the artists performing at our upcoming living-room sessions.</p>

  <article class="abs show" style="top:215px">
    <div class="photo" role="img" aria-label="Photo of a singer-songwriter playing an acoustic guitar" style="background:linear-gradient(135deg,#cfc7c0,#8a6a55)"></div>
    <div class="info"><h3>Clara Whitfield</h3><div class="role">FOLK SINGER-SONGWRITER</div><div class="desc">Excepteur sint occaecat cupidatat non proident, sunt in culpa qui officia</div><a href="#" class="link">Book A Show</a></div>
  </article>
  <article class="abs show" style="top:472px">
    <div class="photo" role="img" aria-label="Close-up photo of hands playing a keyboard under purple light" style="background:linear-gradient(135deg,#3a1040,#b02a5a,#2a0a30)"></div>
    <div class="info"><h3>Marcus Bell</h3><div class="role">INDIE ROCK &amp; ACOUSTIC</div><div class="desc">Excepteur sint occaecat cupidatat non proident, sunt in culpa qui officia</div><a href="#" class="link">Book A Show</a></div>
  </article>
  <article class="abs show" style="top:729px">
    <div class="photo" role="img" aria-label="Close-up photo of hands adjusting knobs on a mixing console" style="background:linear-gradient(135deg,#6a7a8a,#1a2028,#3a6aa0)"></div>
    <div class="info"><h3>Nora Hale</h3><div class="role">FOLK SINGER-SONGWRITER</div><div class="desc">Excepteur sint occaecat cupidatat non proident, sunt in culpa qui officia</div><a href="#" class="link">Book A Show</a></div>
  </article>
</section>
<a href="#" class="abs btn btn-white all-shows">VIEW ALL SHOWS</a>

<section>
  <h2 class="abs display reviews-title">WHAT OUR CUSTOMER SAYS</h2>

  <article class="abs review" style="left:-364px">
    <div class="quote">”</div>
    <div class="stars"><svg width="80" height="13" viewBox="0 0 80 13" fill="var(--gold)"><use href="#star"/><use href="#star" x="16"/><use href="#star" x="32"/><use href="#star" x="48"/><use href="#star" x="64"/></svg></div>
    <h4>Dalton Reyes</h4>
    <p>Every evening here has been special. The room fills with warmth, the music leads us somewhere new, and the hosts make everyone feel welcome, friendly and at home.</p>
    <div class="sign">Thanks, Birchwater</div>
  </article>

  <article class="abs review" style="left:111px">
    <div class="quote">”</div>
    <div class="stars"><svg width="80" height="13" viewBox="0 0 80 13" fill="var(--gold)"><use href="#star"/><use href="#star" x="16"/><use href="#star" x="32"/><use href="#star" x="48"/><use href="#star" x="64"/></svg></div>
    <h4>Pinecrest Paving</h4>
    <p>"The Birchwater Evenings feels like you're discovering music for the first time again. The room is quiet, the lighting is beautiful, and the artists are so close you can feel every lyric. It's easily my favorite way to experience live music in Denver."</p>
    <div class="sign">Thanks, Birchwater</div>
  </article>

  <article class="abs review" style="left:591px">
    <div class="quote">”</div>
    <div class="stars"><svg width="80" height="13" viewBox="0 0 80 13" fill="var(--gold)"><use href="#star"/><use href="#star" x="16"/><use href="#star" x="32"/><use href="#star" x="48"/><use href="#star" x="64"/></svg></div>
    <h4>Dalton Reyes</h4>
    <p>I couldn't believe how special and personal these shows are. It felt like sitting among friends, even though it was my first time attending. The atmosphere is warm, calm, and honestly magical. I'll be RSVPing for every session I can."</p>
    <div class="sign">Thanks, Birchwater</div>
  </article>

  <article class="abs review" style="left:1067px">
    <div class="quote">”</div>
    <div class="stars"><svg width="80" height="13" viewBox="0 0 80 13" fill="var(--gold)"><use href="#star"/><use href="#star" x="16"/><use href="#star" x="32"/><use href="#star" x="48"/><use href="#star" x="64"/></svg></div>
    <h4>Brightpath Leads</h4>
    <p>Brightpath Leads has been a game changer for our asphalt business, delivering cutting-edge strategies and high-quality leads that grew our revenue.</p>
    <div class="sign">Thanks, Birchwater</div>
  </article>

  <div class="abs dots"><span></span><span></span><span class="on"></span><span></span><span></span></div>
</section>

<footer>
  <div class="abs footer"></div>
  <section class="abs cta">
    <h2 class="display">EXPERIENCE LIVE MUSIC<br>UP CLOSE</h2>
    <p>Featuring singer-songwriters, indie artists, and acoustic performers in a quiet, attentive listening space.</p>
  </section>
  <a href="#" class="abs btn btn-white cta-btn">RESERVE YOUR SEAT</a>

  <div class="abs brand foot-brand"><span class="dot"></span><span>The Birchwater<br>Evenings</span></div>
  <nav class="foot-links">
    <a href="#" style="left:596px">Home</a>
    <a href="#" style="left:703px">About Us</a>
    <a href="#" style="left:839px">Contact Us</a>
  </nav>
  <div class="abs copy">Copyrights 2026 The Birchwater. All Rights Reserved</div>
</footer>
</body>
</html>
```